redesing professional certificate

Redesign our certificate to more a professional look and to make it look like a-wanna have - Best in adobe photoshop, because this template will be our basic, and we have in our education different levels, basic, upper, lower, complex, master level. I usually add a small picture to show what level they are. Or when you have a better suggestion I a gladly to hear.
We teach to physiotherapist so it has to look professional.

Target Market(s)

physiotherapist

Industry/Entity Type

Health Care

Requirements
Must have
• our logo

```html
<!DOCTYPE html>
<html lang="en">
<head>
<meta charset="utf-8">
<title>Certificate – Fasciatherapy Level I</title>
<link rel="stylesheet" href="https://fonts.googleapis.com/css2?family=Arimo:ital,wght@0,400;0,700;1,400&family=Kaushan+Script&family=Playfair+Display:wght@400&display=swap">
<style>
  :root {
    --paper: #ffffff;
    --ink-navy: #1b2450;
    --ink-blue: #1f2a8c;
    --band-light: #bcd9ef;
    --band-mid: #6fa6d6;
    --band-deep: #2a5f9e;
    --illus-green: #6f8f4a;
    --illus-orange: #c9772f;
  }
  * { margin: 0; padding: 0; box-sizing: border-box; }
  html, body { width: 996px; height: 1200px; overflow: hidden; background: var(--paper); }
  .certificate {
    position: relative; width: 996px; height: 1200px;
    background: var(--paper); color: var(--ink-blue);
    font-family: "Arimo", Arial, sans-serif;
  }
  .decor-band { position: absolute; inset: 0; width: 996px; height: 1200px; }
  .title {
    position: absolute; left: 90px; top: 185px;
    font-family: "Playfair Display", Georgia, serif; font-weight: 400;
    font-size: 86px; line-height: 1; letter-spacing: 1px; color: var(--ink-navy);
    white-space: nowrap;
  }
  .brand {
    position: absolute; left: 745px; top: 150px; width: 210px;
    display: flex; flex-direction: column; align-items: center; gap: 10px;
  }
  .brand-mark { width: 120px; height: 120px; border-radius: 50%; background: var(--ink-navy); }
  .brand-name {
    font-size: 16px; font-weight: 700; color: var(--ink-navy);
    text-align: center; line-height: 1.25;
  }
  .recipient {
    position: absolute; left: 100px; width: 880px; top: 350px; text-align: center;
    font-family: "Kaushan Script", cursive; font-size: 50px; color: var(--ink-navy);
  }
  .statement {
    position: absolute; left: 100px; width: 880px; top: 425px; text-align: center;
    font-size: 28px; line-height: 40px;
  }
  .statement .strong { font-weight: 700; color: var(--ink-navy); }
  .signatory { position: absolute; text-align: center; font-size: 20px; line-height: 28px; }
  .signatory .name { font-weight: 700; color: var(--ink-navy); }
  .signatory .role { font-style: italic; }
  .signatory--left { left: 250px; top: 620px; width: 280px; }
  .signatory--right { left: 640px; top: 605px; width: 280px; }
  .registration { position: absolute; left: 230px; top: 765px; font-size: 25px; }
  .maintenance {
    position: absolute; left: 230px; top: 825px; width: 660px;
    font-size: 25px; line-height: 36px;
  }
  .issuer {
    position: absolute; left: 360px; top: 985px; font-style: normal;
    font-size: 24px; line-height: 32px;
  }
  .tagline { position: absolute; left: 360px; top: 1125px; font-size: 24px; }
  .illustration {
    position: absolute; left: 805px; top: 985px; width: 160px; height: 160px;
    background: radial-gradient(circle at 50% 50%, var(--illus-orange) 0%, var(--illus-green) 55%, #e9ede2 100%);
  }
</style>
</head>
<body>
  <main class="certificate">
    <svg class="decor-band" viewBox="0 0 996 1200" role="img" aria-label="Decorative blue flowing-wave pattern bands">
      <defs>
        <linearGradient id="band-top" x1="0" y1="0" x2="1" y2="1">
          <stop offset="0" stop-color="var(--band-light)"/>
          <stop offset="0.55" stop-color="var(--band-mid)"/>
          <stop offset="1" stop-color="var(--band-deep)"/>
        </linearGradient>
        <linearGradient id="band-bottom" x1="0" y1="0" x2="1" y2="1">
          <stop offset="0" stop-color="var(--band-light)"/>
          <stop offset="0.6" stop-color="var(--band-mid)"/>
          <stop offset="1" stop-color="var(--band-deep)"/>
        </linearGradient>
      </defs>
      <polygon points="600,0 996,0 996,700" fill="url(#band-top)"/>
      <polygon points="0,620 0,1200 250,1200" fill="url(#band-bottom)"/>
    </svg>

    <h1 class="title">CERTIFICATE</h1>

    <div class="brand">
      <span class="brand-mark"></span>
      <span class="brand-name">Myofascial Balance Method</span>
    </div>

    <p class="recipient">Lucas Moreno</p>

    <p class="statement">
      has completed the fasciatherapy <span class="strong">level I</span> course<br>
      <span class="strong">- 3 days, 15-17 february 2020 -</span><br>
      <span class="strong">Kapavogur, Iceland 17 february 2020.</span>
    </p>

    <div class="signatory signatory--left">
      <div class="name">Mr. JT van Dalen</div>
      <div class="role">Co Director</div>
    </div>
    <div class="signatory signatory--right">
      <div class="name">Mr. RB Haddad</div>
      <div class="role">Co-Director</div>
    </div>

    <p class="registration">Registration Number : 1 ICE 20</p>

    <p class="maintenance">
      The Myofascial Balance Method ongoing certification is contingent upon meeting the requirements of the maintenance of the certification of Fasciatherapy
    </p>

    <address class="issuer">
      Fasciora Academy BV<br>
      Lindengracht 118<br>
      1015KM Amsterdam<br>
      The Netherlands
    </address>

    <p class="tagline">Specialists in fasciatherapy innovation</p>

    <div class="illustration" role="img" aria-label="Illustration of a tensegrity structure of rods and connecting lines"></div>
  </main>
</body>
</html>
```